Boat business cards

I'm looking for business cards with the two logos I've attached. I don't have an specific idea in mind and open to anything. All the usual info will be on the card. Name, position in company, nr, email, address, ect. The company rents out these two boats for charters and fishing.

```html
<!DOCTYPE html>
<html lang="en">
<head>
<meta charset="utf-8">
<title>Aurora Vessel – Business Cards</title>
<link href="https://fonts.googleapis.com/css2?family=Barlow:wght@400;500;600&family=Roboto:wght@400&display=swap" rel="stylesheet">
<style>
  :root {
    --bg: #d6d6d6;
    --card: #ffffff;
    --blue: #5b8fd6;
    --brown: #8b6d47;
    --ink: #1f1f1f;
    --grey: #6b6b6b;
    --rule: #4a4a4a;
  }
  * { margin: 0; padding: 0; box-sizing: border-box; }
  html, body { width: 1200px; height: 800px; overflow: hidden; }
  body {
    background: radial-gradient(ellipse at 40% 20%, #e6e6e6, var(--bg) 70%);
    position: relative;
    font-family: "Roboto", sans-serif;
  }
  .card {
    position: absolute;
    left: 300px;
    width: 600px;
    height: 343px;
    background: var(--card);
    border-radius: 20px;
    overflow: hidden;
    box-shadow: 0 6px 18px rgba(0,0,0,0.18);
  }
  .card--front { top: 28px; }
  .card--back { top: 429px; }
  .wave { position: absolute; inset: 0; width: 600px; height: 343px; }

  .logo { position: absolute; text-align: center; }
  .logo__art { border-radius: 4px; }
  .logo__name {
    font-family: "Barlow", sans-serif;
    font-weight: 600;
    font-size: 22px;
    letter-spacing: 1px;
    color: var(--ink);
    margin-top: 6px;
    white-space: nowrap;
  }
  .logo--aurora .logo__art {
    width: 190px; height: 78px;
    background: linear-gradient(170deg, #e4e6ea 0%, #2b2b2b 38%, #9a7a50 62%, #c9d7ef 100%);
  }
  .logo--tide .logo__art {
    width: 180px; height: 78px;
    background: linear-gradient(170deg, #e8eaee 0%, #b9bec7 30%, #6f9ad8 60%, #5b8fd6 100%);
  }
  .logo--tide .logo__name { color: #4a4a4a; }

  .card--front .logo--aurora { left: 40px; top: 52px; }
  .card--front .logo--tide { left: 370px; top: 26px; }

  .person {
    position: absolute;
    left: 60px;
    top: 190px;
    font-family: "Barlow", sans-serif;
    text-align: right;
    width: 200px;
  }
  .person__name {
    font-weight: 500;
    font-size: 26px;
    letter-spacing: 1px;
    color: var(--brown);
  }
  .person__role {
    font-weight: 400;
    font-size: 17px;
    color: var(--grey);
    margin-top: -2px;
  }
  .divider {
    position: absolute;
    left: 285px;
    top: 138px;
    width: 1px;
    height: 100px;
    background: var(--rule);
  }
  .contact {
    position: absolute;
    left: 300px;
    top: 135px;
    list-style: none;
    font-size: 13.5px;
    line-height: 18px;
    color: var(--grey);
  }
  .contact__item { display: flex; align-items: flex-start; gap: 7px; }
  .contact__icon { width: 12px; height: 12px; margin-top: 3px; flex: none; }

  .card--back .logo--aurora { left: 120px; top: 178px; }
  .card--back .logo--tide { left: 350px; top: 110px; }
</style>
</head>
<body>

<section class="card card--front" aria-label="Business card front">
  <svg class="wave" viewBox="0 0 600 343" aria-hidden="true">
    <path d="M60,343 C220,330 320,300 410,255 C490,215 545,205 600,200"
          fill="none" stroke="var(--blue)" stroke-width="7"/>
    <path d="M90,343 C240,335 335,310 420,268 C500,228 550,218 600,214 L600,343 Z"
          fill="var(--brown)"/>
  </svg>

  <div class="logo logo--aurora">
    <div class="logo__art" role="img" aria-label="Illustration of a motor yacht for Aurora Vessel"></div>
    <div class="logo__name">AURORA VESSEL</div>
  </div>

  <div class="logo logo--tide">
    <div class="logo__art" role="img" aria-label="Illustration of a sport fishing boat for Tide Runner"></div>
    <div class="logo__name">TIDE RUNNER</div>
  </div>

  <div class="person">
    <div class="person__name">DANIEL REYES</div>
    <div class="person__role">President</div>
  </div>

  <div class="divider"></div>

  <ul class="contact">
    <li class="contact__item">
      <svg class="contact__icon" viewBox="0 0 12 12" aria-hidden="true">
        <path d="M6,0.5 C3.5,0.5 2,2.3 2,4.4 C2,7.2 6,11.5 6,11.5 C6,11.5 10,7.2 10,4.4 C10,2.3 8.5,0.5 6,0.5 Z" fill="var(--brown)"/>
        <circle cx="6" cy="4.4" r="1.5" fill="#fff"/>
      </svg>
      <span>2140 Harbor View Road<br>Seward, Alaska 99664</span>
    </li>
    <li class="contact__item">
      <svg class="contact__icon" viewBox="0 0 12 12" aria-hidden="true">
        <rect x="2" y="0.8" width="8" height="10.4" rx="1.2" fill="none" stroke="var(--ink)" stroke-width="1.2"/>
      </svg>
      <span>412-555-0193</span>
    </li>
    <li class="contact__item">
      <svg class="contact__icon" viewBox="0 0 12 12" aria-hidden="true">
        <rect x="0.5" y="2" width="11" height="8" fill="var(--brown)"/>
        <path d="M0.5,2 L6,6.5 L11.5,2" fill="none" stroke="#fff" stroke-width="1"/>
      </svg>
      <span>info@aurorafleet.com</span>
    </li>
  </ul>
</section>

<section class="card card--back" aria-label="Business card back">
  <div class="logo logo--aurora">
    <div class="logo__art" role="img" aria-label="Illustration of a motor yacht for Aurora Vessel"></div>
    <div class="logo__name">AURORA VESSEL</div>
  </div>
  <div class="logo logo--tide">
    <div class="logo__art" role="img" aria-label="Illustration of a sport fishing boat for Tide Runner"></div>
    <div class="logo__name">TIDE RUNNER</div>
  </div>
</section>

</body>
</html>
```